Copper Lantern Haulage

We are a 3PL freight brokerage company looking to create a website to attract new customers. Some ideas on how other freight websites look is located at these links, https://www.bluefinchcarriers.example/services, https://marlowcargo.example/freight-brokerage/.
We would like to have a quote feature implemented into this website.

We specialize in heavy-haul, specialized loads, flatbed, and dry vans.

```html
<!DOCTYPE html>
<html lang="en">
<head>
<meta charset="utf-8">
<title>Copper Lantern Haulage — Transportation and Logistics Solutions</title>
<link href="https://fonts.googleapis.com/css2?family=Montserrat:wght@400;500;600;700&display=swap" rel="stylesheet">
<style>
:root{
  --navy:#16365f;
  --navy-deep:#102a4c;
  --gold:#b8942f;
  --gold-light:#d1ad45;
  --ink:#1c1c1c;
  --muted:#7a7a7a;
  --panel:#f5f5f5;
  --dark:#2a2a2a;
  --darker:#1f1f1f;
  --white:#ffffff;
}
*{box-sizing:border-box;margin:0;padding:0}
html,body{width:1200px;height:4725px;overflow:hidden}
body{position:relative;font-family:'Montserrat',sans-serif;color:var(--ink);background:var(--white)}
.abs{position:absolute}
a{color:inherit;text-decoration:none}

/* header */
.site-header{position:absolute;left:0;top:0;width:1200px;height:128px;background:var(--white);z-index:2}
.brand{position:absolute;left:110px;top:44px;display:flex;align-items:center;gap:10px;font-weight:700;color:var(--navy);font-size:17px;letter-spacing:.5px;line-height:1.15}
.brand-square{width:14px;height:14px;background:var(--gold);flex:none}
.main-nav{position:absolute;left:423px;top:30px;display:flex;gap:26px;font-size:15px;font-weight:500}
.header-call{position:absolute;left:882px;top:18px;display:flex;align-items:center;gap:12px}
.header-call small{display:block;font-size:12px;color:var(--muted)}
.header-call strong{display:block;font-size:19px;color:var(--navy);font-weight:700}

/* hero */
.hero{position:absolute;left:0;top:128px;width:1200px;height:508px;background:linear-gradient(100deg,#3b3630 0%,#6d6457 40%,#8e7f6c 60%,#4a3e38 100%)}
.hero-tag{position:absolute;left:120px;top:98px;font-size:14px;font-weight:600;color:var(--gold-light)}
.hero-title{position:absolute;left:120px;top:128px;font-size:41px;line-height:52px;color:var(--white);font-weight:400;letter-spacing:.5px}
.hero-title b{font-weight:700}
.btn-slant{position:absolute;display:flex;align-items:center;justify-content:center;font-weight:700;font-size:14px;color:var(--white);background:var(--gold);clip-path:polygon(14% 0,100% 0,86% 100%,0 100%)}
.hero .btn-slant{left:120px;top:332px;width:210px;height:56px}
.hero-line{position:absolute;left:80px;top:360px;width:70px;height:1px;background:var(--white)}

/* section headings */
.sec-mark{position:absolute;width:20px;height:20px;background:var(--gold)}
.sec-label{position:absolute;font-size:15px;font-weight:500;letter-spacing:.5px;display:flex;align-items:center;gap:10px}
.sec-label i{display:inline-block;width:40px;height:5px;border-top:1px solid var(--gold);border-bottom:1px solid var(--navy)}
.sec-title{position:absolute;width:1200px;left:0;text-align:center;font-size:31px;font-weight:700}

/* services */
.card{position:absolute;top:870px;width:218px;height:313px;background:var(--white);box-shadow:0 2px 12px rgba(0,0,0,.1);text-align:center}
.card-photo{height:189px;width:100%}
.card-hex{position:absolute;left:89px;top:166px}
.card h3{margin-top:18px;font-size:13px;font-weight:700;color:var(--navy)}
.card p{margin:8px 14px 0;font-size:11px;line-height:17px;color:var(--muted)}
.card .more{display:block;margin-top:10px;font-size:11px;color:var(--gold);font-weight:500}
.card.feature{background:var(--navy)}
.card.feature h3,.card.feature p,.card.feature .more{color:var(--white)}

/* about */
.about-panel{position:absolute;left:112px;top:1302px;width:471px;height:530px;background:var(--navy);color:var(--white);padding:80px 62px 0 63px}
.about-panel .kicker{font-size:14px;letter-spacing:.5px;display:flex;align-items:center;gap:10px}
.about-panel .kicker i{display:inline-block;width:40px;height:5px;border-top:1px solid #8aa0c0;border-bottom:1px solid #8aa0c0}
.about-panel h2{margin-top:16px;font-size:31px;line-height:42px;font-weight:700;padding-left:46px;position:relative}
.about-panel h2::before{content:"";position:absolute;left:0;top:12px;width:22px;height:22px;background:var(--white)}
.about-panel p{margin-top:22px;font-size:13px;line-height:21px}
.about-panel p + p{margin-top:10px}
.about-panel .more{display:flex;align-items:center;gap:12px;margin-top:22px;color:var(--gold-light);font-weight:700;font-size:14px}
.about-photo{position:absolute;left:583px;top:1302px;width:617px;height:530px;background:linear-gradient(120deg,#d9d4cc,#9aa6b2 55%,#e7e2d9)}

/* carriers */
.carrier-box{position:absolute;left:112px;top:2081px;width:969px;height:328px;background:var(--panel)}
.carrier-text{position:absolute;left:72px;top:42px;width:310px;font-size:14px;line-height:22px;color:#333}
.carrier-text p + p{margin-top:18px}
.carrier-box .btn-slant{left:62px;top:231px;width:200px;height:55px}
.carrier-photo{position:absolute;left:590px;top:2088px;width:484px;height:316px;background:linear-gradient(110deg,#c9b79d,#8c7a64 45%,#3c4d66)}

/* achievements */
.achievements{position:absolute;left:0;top:2534px;width:1200px;height:487px;background:linear-gradient(180deg,#1d1d1d,#2e2a24 60%,#1a1a1a);color:var(--white)}
.stat{position:absolute;top:0;width:200px;text-align:center}
.stat-hex{position:absolute;top:252px;left:73px}
.stat strong{position:absolute;top:340px;width:200px;left:0;font-size:33px;font-weight:700}
.stat span{position:absolute;top:382px;width:200px;left:0;font-size:15px}
.stat-divider{position:absolute;top:280px;width:1px;height:120px;background:rgba(255,255,255,.2)}

/* testimonials */
.t-label{position:absolute;left:112px;top:3143px;font-size:14px;display:flex;align-items:center;gap:10px}
.t-label i{display:inline-block;width:40px;height:5px;border-top:1px solid var(--gold);border-bottom:1px solid var(--navy)}
.t-title{position:absolute;left:112px;top:3176px;display:flex;align-items:center;gap:26px;font-size:31px;font-weight:700}
.t-title span.sq{width:22px;height:22px;background:var(--gold)}
.rating{position:absolute;left:686px;top:3192px;font-size:14px;color:#333}
.rating .stars{color:var(--gold-light);letter-spacing:1px;margin-right:8px}
.rating b{color:var(--gold);font-weight:600}
.review{position:absolute;top:3254px;width:308px;height:194px;background:var(--white);box-shadow:0 2px 12px rgba(0,0,0,.1)}
.review p{position:absolute;left:22px;top:38px;width:266px;font-size:13px;line-height:21px;color:#555}
.review .dot{position:absolute;right:18px;top:14px;width:16px;height:16px;border-radius:50%;border:2px solid #c9c9c9}
.avatar{position:absolute;top:3448px;width:48px;height:48px;border-radius:50%;border:3px solid var(--gold);background:#d8c4a8}
.reviewer{position:absolute;top:3496px;width:308px;text-align:center;font-size:15px;color:#333;line-height:19px}
.reviewer small{display:block;font-size:14px;color:#555}
.dots{position:absolute;left:568px;top:3574px;display:flex;gap:4px;align-items:center}
.dots i{width:4px;height:4px;border-radius:50%;background:#ccc}
.dots i.on{width:24px;border-radius:2px;background:var(--gold)}

/* map + quote */
.map{position:absolute;left:0;top:3664px;width:528px;height:407px;background:linear-gradient(135deg,#ececec,#e2e2e2)}
.contact-band{position:absolute;left:0;top:4071px;width:1200px;height:258px;background:linear-gradient(90deg,var(--navy-deep),#1f3e6c)}
.contact-band h2{position:absolute;left:112px;top:88px;font-size:25px;font-weight:700;color:var(--white)}
.contact-band p{position:absolute;left:112px;top:132px;width:560px;font-size:13px;line-height:21px;color:#dfe6f0}
.contact-band .btn-slant{left:779px;top:136px;width:185px;height:55px;background:var(--white);color:var(--gold)}
.contact-band .lead{position:absolute;left:755px;top:163px;width:40px;height:1px;background:var(--white)}
.quote{position:absolute;left:528px;top:3664px;width:557px;height:407px;background:var(--dark);color:var(--white);padding:40px 58px 0 60px;z-index:1}
.quote h2{font-size:31px;line-height:38px;font-weight:700;display:flex;align-items:center;gap:22px}
.quote h2 span{width:20px;height:20px;background:var(--white)}
.quote .intro{margin-top:12px;font-size:13px;font-weight:700;line-height:21px}
.field{background:var(--white);border:1px solid #ccc;height:36px;font-size:11px;color:#888;padding:10px 12px}
.field em{color:#c0392b;font-style:normal}
.row{display:flex;gap:12px;margin-top:20px}
.row .field{flex:1}
.quote .btn-slant{left:60px;top:345px;width:180px;height:42px;font-size:14px}
.quote .lead{position:absolute;left:34px;top:366px;width:40px;height:1px;background:var(--gold)}

/* footer */
.site-footer{position:absolute;left:0;top:4329px;width:1200px;height:288px;background:var(--dark);color:var(--white)}
.foot-brand{position:absolute;left:110px;top:60px;width:210px;text-align:center}
.foot-brand .name{font-size:17px;font-weight:700;line-height:21px}
.foot-brand p{margin-top:16px;font-size:11px;line-height:16px;color:#ccc}
.socials{display:flex;gap:14px;justify-content:center;margin-top:20px}
.socials i{width:24px;height:24px;border-radius:50%;background:var(--white)}
.foot-col{position:absolute;top:56px}
.foot-col h4{font-size:15px;font-weight:700;margin-bottom:18px}
.foot-col li{list-style:none;font-size:14px;line-height:30px;color:#ddd}
.foot-col li::before{content:"›";color:var(--gold);margin-right:12px}
.info{display:flex;gap:16px;margin-bottom:20px;align-items:flex-start}
.info b{display:block;font-size:13px}
.info span{display:block;font-size:11px;color:#ccc;line-height:15px;margin-top:2px;width:170px}
.bottom-bar{position:absolute;left:0;top:4617px;width:1200px;height:108px;background:var(--darker);color:#ccc;font-size:11px}
.bottom-bar .copy{position:absolute;left:117px;top:45px}
.bottom-bar .copy a{color:var(--gold);text-decoration:underline}
.bottom-bar .legal{position:absolute;right:115px;top:45px}
</style>
</head>
<body>

<header class="site-header">
  <div class="brand"><span class="brand-square"></span><span>COPPER LANTERN<br>HAULAGE</span></div>
  <nav class="main-nav"><a href="#">Home</a><a href="#">About Us</a><a href="#">Services</a><a href="#">Carriers</a><a href="#">Contact Us</a></nav>
  <div class="header-call">
    <svg width="34" height="34" viewBox="0 0 24 24" fill="none" stroke="#b8942f" stroke-width="2"><path d="M5 3h4l2 5-3 2a11 11 0 0 0 6 6l2-3 5 2v4a2 2 0 0 1-2 2A17 17 0 0 1 3 5a2 2 0 0 1 2-2z"/></svg>
    <div><small>Call Us Today!</small><strong>(270) 555-0148</strong></div>
  </div>
</header>
<svg class="abs" style="left:0;top:78px;z-index:3" width="1200" height="52" viewBox="0 0 1200 52">
  <polygon points="0,0 360,0 320,50 0,50" fill="#fff"/>
  <polygon points="345,0 372,0 330,50 304,50" fill="#16365f"/>
  <polygon points="378,0 386,0 344,50 336,50" fill="#16365f"/>
  <line x1="360" y1="0" x2="1200" y2="0" stroke="#e5e5e5"/>
</svg>

<section class="hero" role="img" aria-label="Red semi truck hauling a container on a highway at sunset">
  <div class="hero-tag">3PL Freight Brokerage Company</div>
  <h1 class="hero-title">TRANSPORTATION<br>AND LOGISTICS<br><b>SOLUTIONS</b></h1>
  <span class="hero-line"></span>
  <a class="btn-slant" href="#">Get A Quote</a>
</section>

<!-- services -->
<span class="sec-mark" style="left:590px;top:717px"></span>
<div class="sec-label" style="left:510px;top:757px"><i></i>SERVICES<i></i></div>
<h2 class="sec-title" style="top:782px">The Best Services We Provide</h2>

<article class="card" style="left:125px">
  <div class="card-photo" role="img" aria-label="Heavy-haul trailer carrying a large industrial tank" style="background:linear-gradient(160deg,#a9b4c2,#6d7684 60%,#9b8e7b)"></div>
  <svg class="card-hex" width="40" height="44" viewBox="0 0 40 44"><polygon points="20,1 39,12 39,32 20,43 1,32 1,12" fill="#b8942f" stroke="#fff" stroke-width="2"/><rect x="12" y="17" width="16" height="8" fill="#fff"/></svg>
  <h3>HEAVY-HAUL</h3>
  <p>Lorem ipsum dolor sit amet, consectetur adipiscing elit morbi turpis tortor malesuada.</p>
  <a class="more" href="#">Learn More ›</a>
</article>
<article class="card" style="left:368px">
  <div class="card-photo" role="img" aria-label="Oversized specialized load on a multi-axle trailer" style="background:linear-gradient(160deg,#c7c3bb,#8b8578 60%,#c1a03c)"></div>
  <svg class="card-hex" width="40" height="44" viewBox="0 0 40 44"><polygon points="20,1 39,12 39,32 20,43 1,32 1,12" fill="#b8942f" stroke="#fff" stroke-width="2"/><rect x="12" y="17" width="16" height="8" fill="#fff"/></svg>
  <h3>SPECIALIZED LOADS</h3>
  <p>Lorem ipsum dolor sit amet, consectetur adipiscing elit morbi turpis tortor malesuada.</p>
  <a class="more" href="#">Learn More ›</a>
</article>
<article class="card feature" style="left:610px">
  <svg style="margin-top:66px" width="40" height="44" viewBox="0 0 40 44"><polygon points="20,1 39,12 39,32 20,43 1,32 1,12" fill="#b8942f" stroke="#fff" stroke-width="2"/><rect x="12" y="17" width="16" height="8" fill="#fff"/></svg>
  <h3 style="margin-top:6px">FLATBED VANS</h3>
  <p>Lorem ipsum dolor sit amet, consectetur adipiscing elit morbi turpis tortor malesuada. Lorem ipsum dolor sit amet, consectetur adipiscing elit morbi turpis tortor malesuada.</p>
  <a class="more" href="#">Learn More ›</a>
</article>
<article class="card" style="left:854px">
  <div class="card-photo" role="img" aria-label="Red dry van truck on an open road" style="background:linear-gradient(160deg,#b7c3cf,#7b8ea1 55%,#a53a33)"></div>
  <svg class="card-hex" width="40" height="44" viewBox="0 0 40 44"><polygon points="20,1 39,12 39,32 20,43 1,32 1,12" fill="#b8942f" stroke="#fff" stroke-width="2"/><rect x="12" y="17" width="16" height="8" fill="#fff"/></svg>
  <h3>DRY VANS</h3>
  <p>Lorem ipsum dolor sit amet, consectetur adipiscing elit morbi turpis tortor malesuada.</p>
  <a class="more" href="#">Learn More ›</a>
</article>

<!-- about -->
<section class="about-panel">
  <div class="kicker">ABOUT US<i></i></div>
  <h2>We Provide High Quality Logistics Services</h2>
  <p>Lorem ipsum dolor sit amet, consectetur adipiscing elit. Pharetra faucibus fames sed ac volutpat ligula faucibus elit natoque. Ornare ultrices sed nisl vestibulum. In montes, eget mauris non duis nunc. Ultrices lacinia enim.</p>
  <p>Et, nibh tortor pellentesque vestibulum dui. Ac venenatis et egestas est gravida.</p>
  <a class="more" href="#">Learn More <svg width="40" height="10" viewBox="0 0 40 10"><path d="M0 5h38M33 1l5 4-5 4" stroke="#fff" fill="none" stroke-width="1.4"/></svg></a>
</section>
<div class="about-photo" role="img" aria-label="Two warehouse workers checking a parcel with a tablet"></div>

<!-- carriers -->
<span class="sec-mark" style="left:573px;top:1923px"></span>
<div class="sec-label" style="left:496px;top:1962px"><i></i>CARRIERS<i></i></div>
<h2 class="sec-title" style="top:1994px">More Than Just A Delivery</h2>
<section class="carrier-box">
  <div class="carrier-text">
    <p>Vehicula volutpat morbi dolor neque egestas quis. Quam et tincidunt neque at. Neque augue lectus sit.</p>
    <p>Elementum sodales feugiat facilisi nulla. Ultricies tortor, fames nunc quisque dui. Duis cursus tristique sem in sit scelerisque amet varius tellus.</p>
  </div>
  <a class="btn-slant" href="#">Apply Today</a>
</section>
<div class="carrier-photo" role="img" aria-label="Smiling warehouse worker writing on a clipboard among shelves"></div>

<!-- achievements -->
<section class="achievements" role="img" aria-label="Dark mountain highway at dusk behind the achievement figures">
  <span class="sec-mark" style="left:580px;top:50px;background:#fff"></span>
  <div class="sec-label" style="left:487px;top:95px;color:#fff"><i style="border-color:#fff"></i>ACHIEVEMENTS<i style="border-color:#fff"></i></div>
  <h2 class="sec-title" style="top:130px;line-height:42px;color:#fff">We Provide The&nbsp; Highest Level<br>Of Service</h2>

  <div class="stat" style="left:124px"><svg class="stat-hex" width="54" height="60" viewBox="0 0 54 60"><polygon points="27,1 53,15 53,45 27,59 1,45 1,15" fill="#b8942f"/><circle cx="27" cy="23" r="6" fill="#fff"/><rect x="19" y="31" width="16" height="12" rx="3" fill="#fff"/></svg><strong>10+</strong><span>Years of experience</span></div>
  <span class="stat-divider" style="left:349px"></span>
  <div class="stat" style="left:376px"><svg class="stat-hex" width="54" height="60" viewBox="0 0 54 60"><polygon points="27,1 53,15 53,45 27,59 1,45 1,15" fill="#b8942f"/><path d="M14 30l8-6 6 4 6-4 8 6-10 8z" fill="#fff"/></svg><strong>500+</strong><span>Satisfied clients</span></div>
  <span class="stat-divider" style="left:599px"></span>
  <div class="stat" style="left:620px"><svg class="stat-hex" width="54" height="60" viewBox="0 0 54 60"><polygon points="27,1 53,15 53,45 27,59 1,45 1,15" fill="#b8942f"/><rect x="18" y="18" width="18" height="22" rx="3" fill="#fff"/><rect x="21" y="22" width="12" height="6" fill="#b8942f"/></svg><strong>1200+</strong><span>Road trucking</span></div>
  <span class="stat-divider" style="left:848px"></span>
  <div class="stat" style="left:873px"><svg class="stat-hex" width="54" height="60" viewBox="0 0 54 60"><polygon points="27,1 53,15 53,45 27,59 1,45 1,15" fill="#b8942f"/><circle cx="25" cy="20" r="4" fill="#fff"/><path d="M22 27h6l4 8h6v4h-9l-4-7-3 7h-4z" fill="#fff"/></svg><strong>100+</strong><span>Workers in team</span></div>
</section>

<!-- testimonials -->
<div class="t-label">TESTIMONIALS<i></i></div>
<h2 class="t-title"><span class="sq"></span>What Our Customer Say</h2>
<div class="rating"><span class="stars">★★★★★</span>Rated <b>5.0</b> out of <b>5</b> Based on <b>999 reviews</b></div>

<article class="review" style="left:112px"><span class="dot"></span><p>Lorem ipsum dolor sit amet, consectetur adipiscing elit. Scelerisque a malesuada egestas non facilisis risus id nisi, tellus. Sed pellentesque iaculis in varius velit. Eget pellentesque libero, turpis tellus nibh ut tellus.</p></article>
<article class="review" style="left:445px"><span class="dot"></span><p>Lorem ipsum dolor sit amet, consectetur adipiscing elit. Scelerisque a malesuada egestas non facilisis risus id nisi, tellus. Sed pellentesque iaculis in varius velit. Eget pellentesque libero, turpis tellus nibh ut tellus.</p></article>
<article class="review" style="left:777px"><span class="dot"></span><p>Lorem ipsum dolor sit amet, consectetur adipiscing elit. Scelerisque a malesuada egestas non facilisis risus id nisi, tellus. Sed pellentesque iaculis in varius velit. Eget pellentesque libero, turpis tellus nibh ut tellus.</p></article>
<div class="avatar" style="left:242px" role="img" aria-label="Customer portrait"></div>
<div class="avatar" style="left:575px" role="img" aria-label="Customer portrait"></div>
<div class="avatar" style="left:907px" role="img" aria-label="Customer portrait"></div>
<div class="reviewer" style="left:112px">Mara Quillen<small>Lorem ipsum</small></div>
<div class="reviewer" style="left:445px">Mara Quillen<small>Lorem ipsum</small></div>
<div class="reviewer" style="left:777px">Mara Quillen<small>Lorem ipsum</small></div>
<div class="dots"><i class="on"></i><i></i><i></i><i></i><i></i></div>

<!-- quote + contact -->
<div class="map" role="img" aria-label="Street map showing the company office location"></div>
<section class="contact-band">
  <h2>Feel Free To Contact Us</h2>
  <p>Lorem ipsum dolor sit amet, consectetur adipiscing elit. Scelerisque a malesuada egestas non facilisis risus id nisi, tellus. Sed pellentesque iaculis in varius velit. Eget pellentesque libero, turpis tellus nibh ut tellus.</p>
  <span class="lead"></span>
  <a class="btn-slant" href="#">Contact Us</a>
</section>
<section class="quote">
  <h2><span></span>Get A Quote</h2>
  <p class="intro">We will be happy to keep in touch with you and to answer any questions.</p>
  <div class="row"><div class="field">Name <em>*</em></div><div class="field">Phone <em>*</em></div></div>
  <div class="field" style="margin-top:12px">Email <em>*</em></div>
  <div class="field" style="margin-top:12px;height:80px">Write Message here</div>
  <span class="lead"></span>
  <a class="btn-slant" href="#">Get A Quote</a>
</section>

<!-- footer -->
<footer class="site-footer">
  <div class="foot-brand">
    <div class="name">COPPER LANTERN<br>HAULAGE</div>
    <p>Lorem ipsum dolor sit amet, consectetur adipiscing elit pharetra faucibus fames</p>
    <div class="socials"><i></i><i></i><i></i><i></i></div>
  </div>
  <div class="foot-col" style="left:387px"><h4>Quick Links</h4><ul><li>Home</li><li>About Us</li><li>Services</li><li>Carriers</li><li>Contact Us</li></ul></div>
  <div class="foot-col" style="left:586px"><h4>Customer Services</h4><ul><li>Residential Remodels</li><li>Commercial Remodels</li><li>Ground-Up Construction</li></ul></div>
  <div class="foot-col" style="left:861px"><h4>Our Contact Info</h4>
    <div class="info"><svg width="38" height="42" viewBox="0 0 38 42"><polygon points="19,1 37,11 37,31 19,41 1,31 1,11" fill="#b8942f"/><path d="M19 12a6 6 0 0 0-6 6c0 5 6 11 6 11s6-6 6-11a6 6 0 0 0-6-6z" fill="#fff"/></svg><div><b>Location</b><span>418 Harbor Line Ave. Dayton, Ohio 45402</span></div></div>
    <div class="info"><svg width="38" height="42" viewBox="0 0 38 42"><polygon points="19,1 37,11 37,31 19,41 1,31 1,11" fill="#b8942f"/><path d="M13 13h4l1 4-2 1a7 7 0 0 0 4 4l1-2 4 1v4h-2A12 12 0 0 1 12 14z" fill="#fff"/></svg><div><b>Phone</b><span>(270) 555-0148</span></div></div>
    <div class="info"><svg width="38" height="42" viewBox="0 0 38 42"><polygon points="19,1 37,11 37,31 19,41 1,31 1,11" fill="#b8942f"/><rect x="11" y="15" width="16" height="12" fill="#fff"/><path d="M11 15l8 7 8-7" stroke="#b8942f" fill="none"/></svg><div><b>Mail</b><span>dispatch@copperlantern.example</span></div></div>
  </div>
</footer>
<div class="bottom-bar">
  <div class="copy">©Copyright 2022. <a href="#">COPPER LANTERN HAULAGE</a> | All Rights Reserved</div>
  <div class="legal">Privacy Policy &nbsp;|&nbsp; Terms and Conditions</div>
</div>

</body>
</html>
```